Stationery for Family Law Attorney
Business Cards, Envelope, Letterhead
Stationery for Family Law Attorney - Law
Creative Brief
Professional
Marisol K. Denby
Attorney & Counselor at Law
27815 E. Halvorsen Lane Suite 300 San Diego, CA 92984
marisol@counseldenby.example
Exclusively Family Law www.counseldenby.example
MDenby MDenby
Please note the address should read as follows, on the following lines: Line 1: The Quillgate Line 2: 27815 E. Halvorsen Lane Line 3: Suite 610 Line 4: San Diego, CA 92984
Please note the "San Diego, CA 92984" needs to all be on the same line. (858) 555-0147 is the fax line - not the cell. Also, please add the words "The Quillgate" on the line above the 27815 E. Halvorsen Lane line.
Vektor Vektor
sir please check you inbox top right side this web page
Re #37: Please make the back gray. Please replace the symbols with the words for the contact information (i.e. "Phone"). Please remove the website from the front.
Re #30: Please make the "Marisol K. Denby" and "Attorney & Counselor at Law part in small and large caps. Please remove the website from the front of the card. Instead of letters, please write out "Phone" "Fax" and "Email". Thanks. I really like the gray back of the card.

```html
<!DOCTYPE html>
<html lang="en">
<head>
<meta charset="utf-8">
<title>Denby Law Business Card</title>
<link rel="stylesheet" href="https://fonts.googleapis.com/css2?family=Cinzel:wght@400;600&family=Open+Sans:wght@400;600;700&display=swap">
<style>
  :root {
    --backdrop: #b38d33;
    --card-white: #ffffff;
    --card-shade: #eceeef;
    --gray-dark: #4f5153;
    --gray-mid: #6f7275;
    --gray-back-top: #8d8f91;
    --gray-back-bottom: #55585b;
    --teal: #2aa3d2;
    --teal-dark: #127aa3;
    --text: #3a3c3e;
    --rule: #b9bcbf;
  }
  * { margin: 0; padding: 0; box-sizing: border-box; }
  html, body { width: 1200px; height: 686px; overflow: hidden; }
  body {
    background: var(--backdrop);
    font-family: "Open Sans", Arial, sans-serif;
    position: relative;
  }
  .card {
    position: absolute;
    box-shadow: 0 4px 12px rgba(0,0,0,0.35);
  }
  .card-front {
    left: 24px; top: 108px; width: 576px; height: 480px;
    background: linear-gradient(180deg, var(--card-white) 0%, var(--card-white) 60%, var(--card-shade) 100%);
  }
  .card-back {
    left: 612px; top: 173px; width: 564px; height: 367px;
    background: linear-gradient(160deg, var(--gray-back-top) 0%, var(--gray-back-bottom) 100%);
  }
  .firm-mark {
    position: absolute; left: 0; right: 0;
    text-align: center;
    font-family: "Cinzel", "Times New Roman", serif;
    font-weight: 400;
  }
  .card-front .firm-mark { top: 46px; color: var(--gray-dark); }
  .card-back .firm-mark { top: 46px; color: var(--teal); }
  .firm-mark .mark-square {
    display: block; width: 44px; height: 44px; margin: 0 auto 12px;
    background: currentColor;
  }
  .firm-mark .mark-line-small { display: block; font-size: 13px; letter-spacing: 2px; }
  .firm-mark .mark-line-large { display: block; font-size: 34px; line-height: 1.05; letter-spacing: 1px; }
  .firm-mark .mark-line-tag { display: block; font-size: 11px; letter-spacing: 2px; }
  .front-rule {
    position: absolute; left: 90px; width: 396px; top: 196px; height: 2px;
    background: linear-gradient(90deg, transparent, var(--rule), transparent);
  }
  .edge-tab {
    position: absolute; top: 198px; width: 12px; height: 48px;
    background: linear-gradient(180deg, var(--teal) 0%, var(--teal-dark) 100%);
  }
  .edge-tab-left { left: 0; }
  .edge-tab-right { right: 0; }
  .address {
    position: absolute; right: 300px; top: 252px;
    text-align: right; font-size: 13px; line-height: 1.75; color: var(--text);
  }
  .divider {
    position: absolute; left: 288px; top: 252px; width: 1px; height: 100px;
    background: var(--rule);
  }
  .contact {
    position: absolute; left: 300px; top: 250px;
    font-size: 12.5px; line-height: 1.75; color: var(--text);
  }
  .contact .person-name {
    font-variant: small-caps; font-weight: 700; font-size: 17px; color: var(--teal); line-height: 1.4;
  }
  .contact .person-title { font-variant: small-caps; font-weight: 700; }
  .contact .label { color: var(--teal); font-weight: 700; }
  .tagline {
    position: absolute; left: 0; right: 0; top: 202px; text-align: center;
    color: var(--teal); font-weight: 700; font-size: 19px;
  }
  .website {
    position: absolute; left: 0; right: 0; top: 236px; text-align: center;
    color: var(--teal); font-weight: 600; font-size: 12px;
  }
</style>
</head>
<body>
  <section class="card card-front">
    <div class="firm-mark">
      <span class="mark-square"></span>
      <span class="mark-line-small">Law Office of</span>
      <span class="mark-line-large">Marisol K. Denby</span>
      <span class="mark-line-tag">A Professional Corporation</span>
    </div>
    <div class="front-rule"></div>
    <div class="edge-tab edge-tab-left"></div>
    <div class="edge-tab edge-tab-right"></div>
    <div class="address">
      The Quillgate<br>
      27815 E. Halvorsen Lane<br>
      Suite 610<br>
      San Diego, CA 92984
    </div>
    <div class="divider"></div>
    <div class="contact">
      <div class="person-name">Marisol K. Denby</div>
      <div class="person-title">Attorney &amp; Counselor at Law</div>
      <div><span class="label">Phone :</span> (858) 555-0139</div>
      <div><span class="label">Fax :</span> (858) 555-0147</div>
      <div><span class="label">Email :</span> marisol@counseldenby.example</div>
    </div>
  </section>

  <section class="card card-back">
    <div class="firm-mark">
      <span class="mark-square"></span>
      <span class="mark-line-small">Law Office of</span>
      <span class="mark-line-large">Marisol K. Denby</span>
      <span class="mark-line-tag">A Professional Corporation</span>
    </div>
    <div class="tagline">Exclusively Family Law</div>
    <div class="website">www.counseldenby.example</div>
  </section>
</body>
</html>
```